varnomex.com redesign website

This is the current draft version of the website
https://staging1.varnomex.com/
We want:
1. A more professional style in terms of colors, fonts, and structure.
2. Redesign of the diagrams for a better visual experience.
3. The text will remain the same.
4. The single-page structure will also remain, though there will be some secondary pages accessible from the home page, maintaining the same style.
5. We need two pages: 1 Home (with the content of the link above) 2 General template (technical specs, etc)
Examples: https://www.quadmelbin.com/
https://www.brovantile.ai/
Updates
Designs look the same
Target Market(s)
Space, Cybersecurity, robotics, IoT
Industry/Entity Type
Deep Tech Software
Coding
Coded - Design and coding required
Number of Pages Required
2 page
Requirements
Must have
- Demo section, press releases, contact us and footer with GDP
Nice to have
- Team section
Should not have
- Contact phone number

```html
<!DOCTYPE html>
<html lang="en">
<head>
<meta charset="utf-8">
<title>Varnomex Technologies</title>
<link href="https://fonts.googleapis.com/css2?family=Poppins:wght@400;500;600;700&display=swap" rel="stylesheet">
<style>
:root{
  --navy:#2b2a85;
  --navy-deep:#23226f;
  --teal:#1d8cb5;
  --teal-light:#2aa0c8;
  --grey-bg:#f3f3f3;
  --text:#333;
  --muted:#555;
  --white:#fff;
}
*{box-sizing:border-box;margin:0;padding:0}
html,body{width:1200px;height:5296px;overflow:hidden}
body{font-family:'Poppins',sans-serif;color:var(--text);background:var(--white);position:relative}
.abs{position:absolute}
.btn{position:absolute;display:flex;align-items:center;justify-content:center;background:var(--navy);color:#fff;font-weight:600;font-size:16px;border-radius:8px;text-transform:uppercase}
.section-title{position:absolute;color:var(--navy);font-weight:500;font-size:48px;letter-spacing:1px}
.body-text{position:absolute;font-size:14.5px;line-height:26.5px;color:var(--muted);text-align:justify}

/* header */
.site-header{position:absolute;top:0;left:0;width:1200px;height:109px;background:#fff}
.brand{position:absolute;left:68px;top:26px}
.brand-name{font-size:38px;font-weight:600;color:var(--navy);letter-spacing:3px;line-height:1}
.brand-sub{font-size:11px;color:var(--navy);letter-spacing:22px;margin-top:6px}
.main-nav{position:absolute;top:63px;left:478px;display:flex;gap:32px;font-size:12px;color:#333}
.main-nav .active{color:var(--teal);border-bottom:2px solid var(--teal);padding-bottom:6px}
.header-cta{left:997px;top:25px;width:137px;height:27px;font-size:11px;border-radius:5px}

/* hero */
.hero{position:absolute;top:109px;left:0;width:1200px;height:652px;background:linear-gradient(120deg,#0d1530 0%,#1b2448 40%,#3a2a5a 70%,#12182c 100%)}
.hero-title{position:absolute;left:156px;top:126px;color:#fff;font-weight:700;font-size:92px;line-height:106px;letter-spacing:1px}
.hero-sub{position:absolute;left:166px;top:336px;color:#fff;font-size:25px;font-weight:500}
.hero-cta{left:166px;top:403px;width:212px;height:64px;font-size:20px;text-transform:none;border:2px solid #fff;border-radius:10px;background:var(--navy)}
.hero-dots{position:absolute;top:560px;left:570px;display:flex;gap:6px}
.hero-dots span{width:10px;height:10px;border-radius:50%;background:#8c8fb0}
.hero-dots span:first-child{background:#fff}

/* framed media */
.frame-back{position:absolute;background:var(--teal);border-radius:10px}
.media{position:absolute;border-radius:8px}

/* products */
.products{position:absolute;top:1340px;left:0;width:1200px;height:967px;background:var(--grey-bg)}
.product-intro{position:absolute;left:177px;top:192px;width:846px;text-align:center;font-size:12px;line-height:24px;color:var(--muted)}
.node{position:absolute;width:124px;height:124px;border-radius:50%;background:var(--teal)}
.node::after{content:"";position:absolute;inset:6px;border:2px dashed rgba(255,255,255,.85);border-radius:50%}
.node svg{position:absolute;left:37px;top:37px}
.node-label{position:absolute;font-size:19px;line-height:22px;color:#222}
.hub{position:absolute;left:393px;top:436px;width:337px;height:331px;background:var(--navy);border-radius:168px 168px 0 0}
.hub-name{position:absolute;left:0;top:150px;width:100%;text-align:center;color:#fff;font-weight:600;font-size:36px;letter-spacing:2px}

/* explained */
.explained{position:absolute;top:2307px;left:0;width:1200px;height:501px;background:var(--navy)}
.explained h2{position:absolute;top:104px;width:100%;text-align:center;color:#fff;font-weight:500;font-size:44px}
.explained p{position:absolute;top:200px;left:150px;width:900px;text-align:center;color:#fff;font-size:21px;line-height:41px;font-weight:500}
.explained .btn{left:442px;top:318px;width:317px;height:70px;background:var(--teal-light);font-size:25px;text-transform:uppercase}

/* news */
.news{position:absolute;top:3413px;left:0;width:1200px;height:843px;background:var(--grey-bg)}
.news-card{position:absolute;top:232px;width:456px;height:426px}
.news-card .media{left:0;top:0;width:456px;height:251px;border-radius:12px}
.news-card .card-body{position:absolute;left:0;top:192px;width:412px;height:234px;background:var(--grey-bg);border-radius:0 16px 0 0;padding:26px 24px}
.news-date{font-size:12px;color:var(--teal);display:flex;align-items:center;gap:8px}
.news-title{font-size:17px;font-weight:600;color:var(--navy);line-height:21px;margin-top:8px}
.news-text{font-size:11.5px;line-height:21px;color:var(--muted);margin-top:12px}
.read-more{font-size:13px;font-weight:600;font-style:italic;color:var(--teal);text-decoration:underline;margin-top:14px}

/* contact */
.field{position:absolute;background:#fff;box-shadow:0 2px 8px rgba(0,0,0,.14);font-size:11px;color:#999;padding:12px 18px}

/* footer */
.site-footer{position:absolute;top:4903px;left:0;width:1200px;height:393px;background:var(--navy);color:#fff}
.footer-brand{position:absolute;left:72px;top:162px}
.footer-brand .brand-name{color:#fff;font-size:36px}
.footer-brand .brand-sub{color:#fff;font-size:10px;letter-spacing:20px}
.footer-col h3{position:absolute;top:82px;font-weight:500;font-size:19px}
.quick-links{position:absolute;left:454px;top:144px;list-style:none;font-size:14px;line-height:26.3px}
.quick-links li::before{content:"";display:inline-block;width:7px;height:7px;border-radius:50%;background:var(--teal-light);margin-right:14px;vertical-align:middle}
.contact-line{position:absolute;left:672px;display:flex;gap:14px;font-size:13px;line-height:16px}
.contact-line .ico{width:22px;height:22px;background:var(--teal);border-radius:3px;display:flex;align-items:center;justify-content:center}
.copyright{position:absolute;left:72px;top:340px;font-size:12px}
.socials{position:absolute;left:1015px;top:335px;display:flex;gap:6px}
.socials span{width:26px;height:26px;background:#fff;border-radius:3px}
</style>
</head>
<body>

<header class="site-header">
  <div class="brand"><div class="brand-name">VARNOMEX</div><div class="brand-sub">TECHNOLOGIES</div></div>
  <nav class="main-nav">
    <span class="active">Home</span><span>Our Products</span><span>Varnomex Explained</span><span>Applications</span><span>See for Yourself</span><span>News</span><span>About Us</span>
  </nav>
  <div class="btn header-cta">Get in touch</div>
</header>

<section class="hero" role="img" aria-label="Person working on a laptop with glowing data dashboards">
  <h1 class="hero-title">VARNOMEX<br>TECHNOLOGIES</h1>
  <p class="hero-sub">Put Intelligence into your system</p>
  <div class="btn hero-cta">Contact Us</div>
  <div class="hero-dots"><span></span><span></span><span></span><span></span></div>
</section>

<section class="about">
  <div class="frame-back" style="left:127px;top:861px;width:418px;height:360px"></div>
  <div class="media" role="img" aria-label="AI processor chip on a circuit board" style="left:144px;top:878px;width:408px;height:349px;background:linear-gradient(135deg,#1a3aa0,#2a1f7a 60%,#4a1a70)"></div>
  <h2 class="section-title" style="left:633px;top:880px">ABOUT US</h2>
  <p class="body-text" style="left:633px;top:966px;width:440px">Lorem ipsum dolor sit amet, consectetur adipiscing elit. Nullam maximus sollicitudin ipsum sit amet pellentesque. Integer egestas mi et sapien pulvinar efficitur. Orci varius natoque pe natibus et magnis dis parturient montes, nascetur ridiculus mus. Ut fringilla ipsum vel felis posuere, nec pharetra nulla porta. Aenean at malesuada enim.</p>
  <div class="btn" style="left:633px;top:1166px;width:158px;height:49px">Read more</div>
</section>

<section class="products">
  <h2 class="section-title" style="left:0;width:1200px;text-align:center;top:100px">OUR PRODUCTS</h2>
  <p class="product-intro">The Varnomex software framework accelerates the heavy data processing needed to enable AI at the edge on a variety of hardware. The framework resides between the application and OS/HW layer, enabling, based on lock-free programming techniques, acceleration of data processing / AI inference on CPUs, FPGAs, GPUs by fully utilising the available processor resources.</p>

  <div class="hub">
    <div class="hub-name">VARNOMEX</div>
  </div>

  <div class="node" style="left:378px;top:296px"><svg width="50" height="50" viewBox="0 0 50 50" fill="none" stroke="#fff" stroke-width="2"><rect x="8" y="14" width="34" height="22" rx="3"/><path d="M14 40h22M25 36v4M14 20h22M14 26h22"/></svg></div>
  <div class="node-label" style="left:260px;top:342px;text-align:right;width:100px">Varnomex<br>Streaming</div>

  <div class="node" style="left:592px;top:296px"><svg width="50" height="50" viewBox="0 0 50 50" fill="none" stroke="#fff" stroke-width="2"><rect x="6" y="14" width="38" height="28" rx="4"/><circle cx="25" cy="28" r="8"/><path d="M18 14l3-5h8l3 5"/></svg></div>
  <div class="node-label" style="left:735px;top:342px">RBX2<br>Executor plugin</div>

  <div class="node" style="left:257px;top:426px"><svg width="50" height="50" viewBox="0 0 50 50" fill="none" stroke="#fff" stroke-width="2"><rect x="7" y="12" width="36" height="28" rx="3"/><path d="M7 14l18 14 18-14"/><circle cx="25" cy="22" r="5"/></svg></div>
  <div class="node-label" style="left:100px;top:460px;text-align:center;width:130px">Varnomex<br>AI – Artificial<br>Intelligence</div>

  <div class="node" style="left:742px;top:426px"><svg width="50" height="50" viewBox="0 0 50 50" fill="none" stroke="#fff" stroke-width="2"><path d="M10 42L30 20M24 10l2 6 6 2-6 2-2 6-2-6-6-2 6-2z"/><circle cx="38" cy="34" r="3"/><circle cx="40" cy="12" r="2"/></svg></div>
  <div class="node-label" style="left:887px;top:471px">Varnomex Streaming<br>Distribution Optimiser</div>

  <div class="node" style="left:242px;top:602px"><svg width="50" height="50" viewBox="0 0 50 50" fill="none" stroke="#fff" stroke-width="2"><path d="M24 44V18M24 30c-6-2-10-8-8-14 6 2 10 8 8 14zM24 24c4-6 10-8 14-6-2 6-8 8-14 6z"/></svg></div>
  <div class="node-label" style="left:100px;top:648px;text-align:center;width:145px">GPU/FPGA<br>Connector</div>

  <div class="node" style="left:766px;top:602px"><svg width="50" height="50" viewBox="0 0 50 50" fill="none" stroke="#fff" stroke-width="2"><path d="M25 40s12-12 12-20a12 12 0 0 0-24 0c0 8 12 20 12 20z"/><circle cx="25" cy="20" r="4"/><path d="M10 44h30"/></svg></div>
  <div class="node-label" style="left:915px;top:648px">Varnomex<br>in-the-Loop</div>

  <div class="btn" style="left:485px;top:825px;width:158px;height:49px">Know more</div>
</section>

<section class="explained">
  <h2>VARNOMEX EXPLAINED</h2>
  <p>Varnomex – The Software Framework for highly efficient AI inference and data processing to enable Intelligent Space Systems</p>
  <div class="btn">Get in touch</div>
</section>

<section class="demos">
  <h2 class="section-title" style="left:136px;top:2946px">OUR DEMOS</h2>
  <p class="body-text" style="left:136px;top:3022px;width:440px">Lorem ipsum dolor sit amet, consectetur adipiscing elit. Nullam maximus sollicitudin ipsum sit amet pellentesque. Integer egestas mi et sapien pulvinar efficitur. Orci varius natoque pe natibus et magnis dis parturient montes, nascetur ridiculus mus. Ut fringilla ipsum vel felis posuere, nec pharetra nulla porta. Aenean at malesuada enim.</p>
  <div class="btn" style="left:136px;top:3234px;width:160px;height:49px">Know more</div>
  <div class="frame-back" style="left:647px;top:2929px;width:407px;height:354px"></div>
  <div class="media" role="img" aria-label="Edge computing architecture diagram of the software framework" style="left:629px;top:2944px;width:405px;height:348px;background:linear-gradient(160deg,#c4e5ee,#a9d6e3 60%,#d8eef3)"></div>
</section>

<section class="news">
  <h2 class="section-title" style="left:0;width:1200px;text-align:center;top:112px">OUR LATEST NEWS</h2>
  <article class="news-card" style="left:127px">
    <div class="media" role="img" aria-label="Embedded processing board" style="background:linear-gradient(135deg,#2a3a3a,#4b5a5a 50%,#1c2424)"></div>
    <div class="card-body">
      <div class="news-date"><svg width="12" height="12" viewBox="0 0 12 12"><rect x="1" y="2" width="10" height="9" fill="none" stroke="#1d8cb5" stroke-width="1.4"/><path d="M1 5h10" stroke="#1d8cb5" stroke-width="1.4"/></svg>JAN 25, 2023</div>
      <div class="news-title">Varnomex AI successfully ported to KALTOS6 SMP for a Vexon-A9</div>
      <div class="news-text">As part of an ongoing contract with Orvana Space Agency, Varnomex team has recently completed the porting of Varnomex AI to KALTOS6 SMP.</div>
      <div class="read-more">READ MORE</div>
    </div>
  </article>
  <article class="news-card" style="left:619px">
    <div class="media" role="img" aria-label="Satellites orbiting Earth and Moon" style="background:radial-gradient(circle at 70% 60%,#4a6a7a,#1a2530 55%,#0b0f15)"></div>
    <div class="card-body">
      <div class="news-date"><svg width="12" height="12" viewBox="0 0 12 12"><rect x="1" y="2" width="10" height="9" fill="none" stroke="#1d8cb5" stroke-width="1.4"/><path d="M1 5h10" stroke="#1d8cb5" stroke-width="1.4"/></svg>JAN 25, 2023</div>
      <div class="news-title">Varnomex AI successfully ported to KALTOS6 SMP for a Vexon-A9</div>
      <div class="news-text">As part of an ongoing contract with Orvana Space Agency, Varnomex team has recently completed the porting of Varnomex AI to KALTOS6 SMP.</div>
      <div class="read-more">READ MORE</div>
    </div>
  </article>
  <div class="btn" style="left:520px;top:691px;width:160px;height:47px">View more</div>
</section>

<section class="contact">
  <div class="frame-back" style="left:131px;top:4375px;width:418px;height:406px"></div>
  <div class="media" role="img" aria-label="Glowing neon brain made of circuit lines" style="left:150px;top:4392px;width:409px;height:398px;background:radial-gradient(circle at 50% 45%,#3a2a8a,#10124a 60%,#0a0c30)"></div>
  <h2 class="section-title" style="left:652px;top:4380px">CONTACT US</h2>
  <div class="field" style="left:654px;top:4468px;width:199px;height:39px">First Name:</div>
  <div class="field" style="left:870px;top:4468px;width:199px;height:39px">Last Name:</div>
  <div class="field" style="left:654px;top:4525px;width:199px;height:39px">Phone:</div>
  <div class="field" style="left:870px;top:4525px;width:199px;height:39px">Email:</div>
  <div class="field" style="left:654px;top:4583px;width:415px;height:123px">Mesage:</div>
  <div class="btn" style="left:654px;top:4741px;width:168px;height:47px">Submit now</div>
</section>

<footer class="site-footer">
  <div class="footer-brand"><div class="brand-name">VARNOMEX</div><div class="brand-sub">TECHNOLOGIES</div></div>
  <div class="footer-col"><h3 style="left:454px">Quick Links</h3></div>
  <ul class="quick-links"><li>Our Products</li><li>Varnomex Explained</li><li>Applications</li><li>See for Yourself</li><li>News</li><li>About Us</li></ul>
  <div class="footer-col"><h3 style="left:672px">Contact Us</h3></div>
  <div class="contact-line" style="top:148px"><span class="ico"><svg width="12" height="10" viewBox="0 0 12 10"><rect x="0.5" y="0.5" width="11" height="9" fill="none" stroke="#fff"/><path d="M0.5 0.5l5.5 5 5.5-5" fill="none" stroke="#fff"/></svg></span><span>EMAIL US<br>info@varnomex.com</span></div>
  <div class="contact-line" style="top:190px"><span class="ico"><svg width="10" height="13" viewBox="0 0 10 13"><path d="M5 12S1 7.5 1 5a4 4 0 0 1 8 0c0 2.5-4 7-4 7z" fill="#fff"/><circle cx="5" cy="5" r="1.5" fill="#1d8cb5"/></svg></span><span>Address line dummy here<br>Address line dummy here</span></div>
  <div class="footer-col"><h3 style="left:941px">Our Newsletter</h3></div>
  <p class="abs" style="left:941px;top:150px;font-size:13px;line-height:15px">Subscribe our newsletter to<br>get the latest news.</p>
  <div class="abs" style="left:941px;top:196px;width:194px;height:29px;background:#fff"></div>
  <div class="abs" style="left:941px;top:237px;width:98px;height:25px;background:var(--teal);font-size:10px;font-weight:600;display:flex;align-items:center;justify-content:center">SUBSCRIBE</div>
  <div class="copyright">©2024 Varnomex Technologies</div>
  <div class="socials"><span></span><span></span><span></span><span></span></div>
</footer>

</body>
</html>
```